Halcyon Motion a Centre Pty Ltd

Business card is to promote and represent our new business. It's situated in
48 Wren Parade
Brookvale 2100 Sydney
Our clinic is all about getting people back to great health giving them back their lifestyle in half the usual time it takes to get results elsewhere , we do this through innovative therapies with latest state of the art equipment ,skills ,knowledge and experience.
We give them back their pain free healthy lifestyle with lots of energy to love life and perform their best Quickly and effectively .
The final design should communicate
Trust , confidence, results .

Reason: Waiting for some designers to submit work Thanks

Target Market(s)

High end clients that take their health and results seriously ,
High end athletes , as well as general people that want to see results with different
Treatment Methods and approach

Industry/Entity Type

Clinic

Contact Information for Business Card

Halcyon Motion Centre Pty Ltd
48 Wren Parade Brookvale 2100 Sydney
Website www.halcyonmotioncentre.com.au

Font styles to use
Other font styles liked:
• Gothic font medium

Requirements
Must have
• A designe that makes people look twice with a wow factor , a designe that isn't like all the rest .
• Must have the logo in the colours Iv provided in my files
• Must communicate Trust, confidence , results
Nice to have
• 1) The logo raised up or
• 2) Maybe a pop up logo on the card ?
• Or let's be creative and have two cards one on top of the other so the two cards slide .... The front will have the halcyon logo with the address details etc
• The other card with have
• eg your next app .......................................repeating all way down the card
Should not have
• Basic plain looking card that everyone else has

```html
<!DOCTYPE html>
<html lang="en">
<head>
<meta charset="utf-8">
<title>Halcyon Motion Centre – Business Card</title>
<link href="https://fonts.googleapis.com/css2?family=Montserrat:wght@400;500;600;700&display=swap" rel="stylesheet">
<style>
  :root{
    --bg:#ecebe7;
    --card:#ffffff;
    --green-light:#7cc242;
    --green:#4f9a34;
    --green-deep:#3d8a2c;
    --blue:#2f4f9e;
    --blue-light:#3f7fc4;
    --ink:#2d3f8a;
    --ink-soft:#5f6b86;
    --on-green:#ffffff;
  }
  *{margin:0;padding:0;box-sizing:border-box}
  html,body{width:1076px;height:1200px;overflow:hidden}
  body{background:var(--bg);font-family:"Montserrat",sans-serif;position:relative}
  .card{position:absolute;left:108px;width:860px;height:491px;background:var(--card);
        box-shadow:0 14px 34px rgba(0,0,0,.16);overflow:hidden}
  .card--front{top:60px}
  .card--back{top:649px}
  .card-art{position:absolute;inset:0;width:100%;height:100%}

  .brand{position:absolute;display:flex;align-items:center;gap:16px}
  .brand-dot{width:34px;height:34px;border-radius:50%;background:var(--green);flex:none}
  .brand-name{font-weight:700;color:var(--ink);letter-spacing:.5px;white-space:nowrap}
  .card--front .brand{left:50%;top:50%;transform:translate(-50%,-50%)}
  .card--front .brand-name{font-size:38px}
  .card--back .brand{left:52px;top:140px;gap:14px}
  .card--back .brand-name{font-size:26px;line-height:1.2}
  .card--back .brand-dot{width:26px;height:26px}

  .address{position:absolute;left:52px;bottom:58px;display:flex;gap:14px;align-items:flex-start;
           color:var(--ink-soft);font-size:16px;line-height:1.45;font-weight:500}
  .icon{width:26px;height:26px;border-radius:4px;background:var(--blue-light);flex:none;
        display:flex;align-items:center;justify-content:center}
  .icon svg{width:16px;height:16px}

  .person{position:absolute;right:46px;top:50px;text-align:right;color:var(--on-green)}
  .person-name{font-size:30px;font-weight:700;letter-spacing:2px;text-transform:uppercase}
  .person-role{font-size:14px;font-weight:500;letter-spacing:3px;text-transform:uppercase;margin-top:6px;opacity:.9}

  .contacts{position:absolute;right:46px;bottom:54px;list-style:none;color:var(--on-green);
            font-size:15px;font-weight:500}
  .contacts li{display:flex;align-items:center;justify-content:flex-end;gap:12px;margin-top:12px}
  .contacts .icon{width:22px;height:22px;background:var(--on-green)}
  .contacts .icon svg{width:14px;height:14px}
</style>
</head>
<body>

<section class="card card--front" aria-label="Card front">
  <svg class="card-art" viewBox="0 0 860 491" aria-hidden="true">
    <defs>
      <linearGradient id="bandGreen" x1="0" y1="0" x2="1" y2="1">
        <stop offset="0" stop-color="#7cc242"/>
        <stop offset="1" stop-color="#3d8a2c"/>
      </linearGradient>
    </defs>
    <polygon points="0,0 92,0 40,300 0,300" fill="url(#bandGreen)"/>
    <polygon points="92,0 104,0 52,300 40,300" fill="#2f4f9e"/>
    <polygon points="860,491 768,491 820,191 860,191" fill="url(#bandGreen)"/>
    <polygon points="768,491 756,491 808,191 820,191" fill="#2f4f9e"/>
  </svg>
  <div class="brand">
    <span class="brand-dot"></span>
    <span class="brand-name">Halcyon Motion Centre</span>
  </div>
</section>

<section class="card card--back" aria-label="Card back">
  <svg class="card-art" viewBox="0 0 860 491" aria-hidden="true">
    <defs>
      <linearGradient id="panelGreen" x1="0" y1="0" x2="1" y2="1">
        <stop offset="0" stop-color="#7cc242"/>
        <stop offset="1" stop-color="#3d8a2c"/>
      </linearGradient>
      <linearGradient id="stripeBlue" x1="0" y1="0" x2="0" y2="1">
        <stop offset="0" stop-color="#3f7fc4"/>
        <stop offset="1" stop-color="#2f4f9e"/>
      </linearGradient>
    </defs>
    <polygon points="450,0 860,0 860,491 360,491" fill="url(#panelGreen)"/>
    <polygon points="422,0 438,0 348,491 332,491" fill="url(#stripeBlue)"/>
    <polygon points="402,40 412,40 327,491 317,491" fill="#2f4f9e"/>
  </svg>

  <div class="brand">
    <span class="brand-dot"></span>
    <span class="brand-name">Halcyon Motion<br>Centre</span>
  </div>

  <div class="address">
    <span class="icon"><svg viewBox="0 0 16 16"><path d="M8 1a5 5 0 0 0-5 5c0 4 5 9 5 9s5-5 5-9a5 5 0 0 0-5-5zm0 7a2 2 0 1 1 0-4 2 2 0 0 1 0 4z" fill="#fff"/></svg></span>
    <p>48 Wren Parade<br>Brookvale 2100 Sydney</p>
  </div>

  <div class="person">
    <p class="person-name">Aaron Vale</p>
    <p class="person-role">Clinic Director</p>
  </div>

  <ul class="contacts">
    <li>02 9938 4410 <span class="icon"><svg viewBox="0 0 16 16"><path d="M4 1l3 3-2 2c1 2 3 4 5 5l2-2 3 3-2 2C7 14 2 9 2 3z" fill="#3d8a2c"/></svg></span></li>
    <li>0412 660 218 <span class="icon"><svg viewBox="0 0 16 16"><rect x="4" y="1" width="8" height="14" rx="1.5" fill="#3d8a2c"/><rect x="5.5" y="3" width="5" height="8" fill="#fff"/></svg></span></li>
    <li>hello@halcyonmotioncentre.com.au <span class="icon"><svg viewBox="0 0 16 16"><rect x="1" y="3" width="14" height="10" fill="#3d8a2c"/><path d="M1 3l7 6 7-6" stroke="#fff" stroke-width="1.4" fill="none"/></svg></span></li>
    <li>www.halcyonmotioncentre.com.au <span class="icon"><svg viewBox="0 0 16 16"><circle cx="8" cy="8" r="6.5" stroke="#3d8a2c" stroke-width="1.5" fill="none"/><path d="M1.5 8h13M8 1.5c-3 3.5-3 9.5 0 13M8 1.5c3 3.5 3 9.5 0 13" stroke="#3d8a2c" stroke-width="1.2" fill="none"/></svg></span></li>
  </ul>
</section>

</body>
</html>
```